Infographic - Engagement Survey

Infographic required to be used in our marketing collateral and our website

Target Market(s)

B2B - commercial, non for profit, private, government and council

Industry/Entity Type

Marketing

Font styles to use
Sans Serif

Colors
0455a3
3276b5
85abd2
cedeed
e34197

Requirements
Must have
• Please refer to document for branding colours, fonts used are arial, calibri and century gothic

```html
<!DOCTYPE html>
<html lang="en">
<head>
<meta charset="utf-8">
<title>Job, Team, Leader, And Organisation Factors Predicting Engagement</title>
<link href="https://fonts.googleapis.com/css2?family=Questrial&family=Carlito:wght@400;700&family=Mulish:wght@700;800&display=swap" rel="stylesheet">
<style>
  :root {
    --navy: #1a3a9c;
    --brand-blue: #0455a3;
    --mid-blue: #3276b5;
    --soft-blue: #85abd2;
    --pale-blue: #cedeed;
    --magenta: #e535e8;
    --stripe-magenta: #e34197;
    --stripe-blue: #3a86e0;
    --stripe-light: #c4e8f2;
    --team: #5aaee0;
    --jobs: #b5dcef;
    --leader: #3b8fd6;
    --org: #1e6fd6;
    --chip: #e2f8f0;
    --line: #c9ccd2;
    --dot: #5aaee0;
    --dot-strong: #1f5fe0;
    --text: #2b2b2b;
    --muted: #6a6a6a;
    --table-green: #45e39c;
    --table-teal: #3e8878;
    --row-a: #f3f3f3;
    --row-b: #e6e6e6;
  }
  html, body { margin: 0; padding: 0; overflow: hidden; background: #fff; }
  .canvas {
    position: relative; width: 857px; height: 1200px; overflow: hidden;
    background: #fff; font-family: "Carlito", "Calibri", sans-serif; color: var(--text);
  }
  .header-band {
    position: absolute; left: 86px; top: 12px; width: 523px; height: 105px;
    background: var(--navy);
  }
  .header-title {
    position: absolute; right: 28px; top: 16px; margin: 0;
    font-family: "Questrial", sans-serif; font-weight: 400; font-size: 27px;
    line-height: 31px; color: #fff; text-align: right;
  }
  .brand { position: absolute; left: 609px; top: 12px; width: 188px; height: 105px; }
  .stripe { position: absolute; height: 6px; }
  .stripe.top { top: 0; } .stripe.bottom { bottom: 0; }
  .s1 { left: 0; width: 64px; background: var(--stripe-magenta); }
  .s2 { left: 64px; width: 60px; background: var(--stripe-blue); }
  .s3 { left: 124px; width: 64px; background: var(--stripe-light); }
  .brand-name {
    position: absolute; left: 0; right: 0; top: 38px; text-align: center;
    font-family: "Mulish", sans-serif; font-weight: 800; font-size: 19px;
    line-height: 22px; color: var(--navy);
  }
  .diagram { position: absolute; left: 0; top: 0; width: 857px; height: 820px; }
  .group-label {
    position: absolute; margin: 0; font-family: "Mulish", sans-serif;
    font-weight: 700; font-size: 16px; letter-spacing: .3px;
  }
  .label-team { right: 576px; top: 216px; color: var(--team); }
  .label-jobs { left: 571px; top: 207px; color: var(--jobs); }
  .label-leader { right: 598px; top: 422px; color: var(--leader); }
  .label-org { left: 648px; top: 396px; color: var(--org); }
  .factor-list { position: absolute; margin: 0; padding: 0; list-style: none; }
  .factor-list li {
    position: absolute; white-space: nowrap; font-size: 12.5px; line-height: 16px;
  }
  .factor-list li::before {
    content: ""; position: absolute; top: -1px; bottom: -2px; z-index: -1;
    background: var(--chip); transform: skewX(-28deg);
  }
  .list-right li { right: 0; }
  .list-right li::before { left: -18px; right: -8px; }
  .list-left li { left: 0; }
  .list-left li::before { left: -8px; right: -18px; }
  .list-team { right: 579px; top: 0; }
  .list-leader { right: 579px; top: 0; }
  .list-jobs { left: 583px; top: 0; }
  .list-org { left: 658px; top: 0; }
  .engagement-label {
    position: absolute; left: 0; width: 890px; top: 777px; margin: 0; text-align: center;
    font-family: "Mulish", sans-serif; font-weight: 800; font-size: 24px; color: var(--magenta);
  }
  .summary-title {
    position: absolute; left: 97px; top: 841px; margin: 0;
    font-family: "Questrial", sans-serif; font-weight: 400; font-size: 15px; color: var(--muted);
  }
  table { border-collapse: collapse; font-family: "Questrial", sans-serif; }
  .model-table { position: absolute; left: 97px; top: 871px; width: 302px; font-size: 10px; }
  .model-table th {
    background: var(--table-green); color: #fff; font-weight: 400; height: 37px;
    line-height: 12px; padding: 0 4px;
  }
  .model-table td { background: var(--row-a); height: 32px; text-align: center; color: var(--text); }
  .predictor-table { position: absolute; left: 463px; top: 869px; width: 325px; font-size: 10px; }
  .predictor-table th {
    background: var(--table-teal); color: #fff; font-weight: 400; font-size: 11px;
    height: 37px; text-align: left; padding: 0 12px;
  }
  .predictor-table th.weight, .predictor-table td.weight { text-align: right; padding-right: 17px; }
  .predictor-table td { height: 31.3px; padding: 0 11px; color: var(--text); }
  .predictor-table tr:nth-child(odd) td { background: var(--row-a); }
  .predictor-table tr:nth-child(even) td { background: var(--row-b); }
</style>
</head>
<body>
<div class="canvas">
  <header>
    <div class="header-band">
      <h1 class="header-title">Job, Team, Leader, And Organisation<br>Factors Predicting Engagement</h1>
    </div>
    <div class="brand">
      <span class="stripe top s1"></span><span class="stripe top s2"></span><span class="stripe top s3"></span>
      <div class="brand-name">Corvale<br>Consulting</div>
      <span class="stripe bottom s1"></span><span class="stripe bottom s2"></span><span class="stripe bottom s3"></span>
    </div>
  </header>

  <section class="diagram">
    <svg width="857" height="820" viewBox="0 0 857 820" aria-hidden="false">
      <defs>
        <filter id="soft-shadow" x="-40%" y="-40%" width="180%" height="180%">
          <feDropShadow dx="6" dy="8" stdDeviation="6" flood-color="#000" flood-opacity=".18"/>
        </filter>
      </defs>
      <g fill="none" stroke="var(--line)" stroke-width="1">
        <circle cx="445" cy="655" r="119"/>
        <circle cx="445" cy="655" r="107"/>
        <polyline points="417,229 439,229 439,570"/>
        <polyline points="471,211 453,211 453,570"/>
        <polyline points="363,421 426,421 426,570"/>
        <polyline points="522,408 468,408 468,570"/>
      </g>
      <g fill="none" stroke="#9aa3ad" stroke-width="1" stroke-dasharray="1.5 2">
        <polyline points="355,261 355,297 326,297"/>
        <polyline points="290,258 296,258 296,351 290,351"/>
        <polyline points="517,243 517,291 566,291"/>
        <polyline points="570,247 564,247 564,338 570,338"/>
        <polyline points="318,461 318,559 296,559"/>
        <polyline points="289,476 295,476 295,720 289,720"/>
        <polyline points="587,442 587,515 636,515"/>
        <polyline points="643,444 637,444 637,606 643,606"/>
      </g>
      <g fill="var(--dot)">
        <circle cx="417" cy="229" r="3"/>
        <circle cx="326" cy="297" r="3"/>
        <circle cx="471" cy="211" r="3" fill="var(--pale-blue)"/>
        <circle cx="517" cy="269" r="3" fill="var(--pale-blue)"/>
        <circle cx="453" cy="362" r="3" fill="var(--pale-blue)"/>
        <circle cx="439" cy="409" r="3"/>
        <circle cx="363" cy="421" r="3"/>
        <circle cx="318" cy="506" r="3"/>
        <circle cx="426" cy="467" r="3" fill="var(--dot-strong)"/>
        <circle cx="522" cy="408" r="3" fill="var(--dot-strong)"/>
        <circle cx="468" cy="477" r="3" fill="var(--dot-strong)"/>
        <circle cx="587" cy="484" r="3" fill="var(--dot-strong)"/>
      </g>
      <circle cx="445" cy="655" r="80" fill="var(--magenta)" filter="url(#soft-shadow)" role="img" aria-label="Two interlocking orange gears representing engagement"/>
      <circle cx="344" cy="228" r="33" fill="var(--team)" filter="url(#soft-shadow)" role="img" aria-label="Hands joined together representing team"/>
      <circle cx="517" cy="210" r="32" fill="var(--pale-blue)" filter="url(#soft-shadow)" role="img" aria-label="Briefcase representing jobs"/>
      <circle cx="317" cy="428" r="33" fill="var(--stripe-blue)" filter="url(#soft-shadow)" role="img" aria-label="Business leader representing leadership"/>
      <circle cx="586" cy="409" r="33" fill="#0b4ee0" filter="url(#soft-shadow)" role="img" aria-label="Hand holding a network of nodes representing organisation"/>
    </svg>

    <h2 class="group-label label-team">TEAM</h2>
    <ul class="factor-list list-right list-team">
      <li style="top:248px">optimism</li>
      <li style="top:273px">clarity of goals</li>
      <li style="top:297px">freedom to make decisions</li>
      <li style="top:320px">performance feedback</li>
      <li style="top:343px">customer commitment</li>
    </ul>

    <h2 class="group-label label-jobs">JOBS</h2>
    <ul class="factor-list list-left list-jobs">
      <li style="top:238px">optimism</li>
      <li style="top:261px">self-confidence</li>
      <li style="top:284px">variety of work</li>
      <li style="top:307px">learning of work</li>
      <li style="top:329px">knowledge of processes and policies</li>
    </ul>

    <h2 class="group-label label-leader">LEADER</h2>
    <ul class="factor-list list-right list-leader">
      <li style="top:468px">creates a learning environment</li>
      <li style="top:495px">supports leadership</li>
      <li style="top:522px">fosters teamwork</li>
      <li style="top:549px">encourages autonomous decision making</li>
      <li style="top:576px">creates clarity about appropriate behaviours</li>
      <li style="top:603px">effective management of behaviours</li>
      <li style="top:630px">creates clarity about performance standards</li>
      <li style="top:657px">effective management of underperformance</li>
      <li style="top:684px">celebrates success</li>
      <li style="top:711px">optimism and positivity</li>
    </ul>

    <h2 class="group-label label-org">ORGANISATION</h2>
    <ul class="factor-list list-left list-org">
      <li style="top:435px">performance feedback</li>
      <li style="top:457px">customer commitment</li>
      <li style="top:480px">clarity of goals</li>
      <li style="top:504px">recognition of performance</li>
      <li style="top:527px">optimism</li>
      <li style="top:551px">freedom to make decisions</li>
      <li style="top:574px">willingness to change</li>
      <li style="top:597px">encouragment, support</li>
    </ul>

    <p class="engagement-label">ENGAGEMENT</p>
  </section>

  <section class="model-summary">
    <h2 class="summary-title">MODEL SUMMARY</h2>
    <table class="model-table">
      <tr><th>Model</th><th>R</th><th>R Square</th><th>Adjusted<br>R Square</th><th>Std Error of<br>the Estimate</th></tr>
      <tr><td>1</td><td>.806</td><td>.650</td><td>.641</td><td>.64165</td></tr>
    </table>
  </section>

  <section class="predictors">
    <table class="predictor-table">
      <tr><th>Best predictors of Engagement</th><th class="weight">Beta weights</th></tr>
      <tr><td>(CB) Learning at work</td><td class="weight">.257</td></tr>
      <tr><td>(CB) Optimism - job</td><td class="weight">.238</td></tr>
      <tr><td>(CB) Self confidence</td><td class="weight">.207</td></tr>
      <tr><td>(CB) Variety of work</td><td class="weight">.189</td></tr>
      <tr><td>(LB) Creates a learning environment</td><td class="weight">-.131</td></tr>
      <tr><td>(CB) Optimism - learn</td><td class="weight">.112</td></tr>
      <tr><td>(CB) Clarity of goals - learn</td><td class="weight">.123</td></tr>
      <tr><td>Recognition of performance - learn</td><td class="weight">.103</td></tr>
    </table>
  </section>
</div>
</body>
</html>
```